Business cards / Letterheads / Compliment slips

We are looking to get business cards, letterheads and compliment slips designed.

These will all have to follow the design of our new website and logo. Links to the website, logo and fonts can be found below...

The designs need to be simple with focus on the typography. Only the following colours should be used on the designs...

#7f9d3c
#191818
#fff

Website:
http://brookfieldweb.examplestudio.co.uk/

Logo:
https://www.filecrate.example/sh/8kd2m4qwzpla7ve/hTr5NpQ2Xw/logos

Fonts:
https://www.filecrate.example/sh/8kd2m4qwzpla7ve/Q9vTzR3mKe/Fonts/BayerModern_TTF

and

https://www.filecrate.example/sh/8kd2m4qwzpla7ve/W7nHcY5pD3/Fonts/MuseoSansFamily

Reason: We would like some more design submissions

Reason: We are still deciding on designs we like and would like to see some more submissions...

Industry/Entity Type

Business

Requirements
Must have
• The designs need to be simple with focus on the typography. Only the following colours should be used on the designs...

#7f9d3c
#191818
#fff
Should not have
• - Any fonts that are not provided.
- Any colours that are not provided.

```html
<!DOCTYPE html>
<html lang="en">
<head>
<meta charset="utf-8">
<title>Brookfieldweb Stationery</title>
<link rel="stylesheet" href="https://fonts.googleapis.com/css2?family=Mulish:wght@300;400;500;700&display=swap">
<style>
  :root {
    --green: #7f9d3c;
    --ink: #191818;
    --card-dark: #333232;
    --paper: #ffffff;
    --backdrop: #f7f7f7;
    --muted: #cfcfcf;
  }
  * { margin: 0; padding: 0; box-sizing: border-box; }
  html, body { width: 1200px; height: 900px; overflow: hidden; }
  body {
    background: var(--backdrop);
    font-family: "Mulish", Arial, sans-serif;
    color: var(--ink);
    position: relative;
  }
  .sheet {
    position: absolute;
    background: var(--paper);
    box-shadow: 0 0 4px rgba(0,0,0,0.25);
  }
  .brand {
    position: absolute;
    display: flex;
    align-items: center;
    gap: 8px;
  }
  .brand-name {
    font-weight: 700;
    color: var(--ink);
    letter-spacing: -0.5px;
    line-height: 1;
  }
  .office { color: var(--green); }
  .address { line-height: 1.2; }
  .phone { color: var(--green); }
  .web-accent { color: var(--green); }
  .rule { position: absolute; height: 1px; background: var(--green); opacity: 0.8; }

  /* Letterhead */
  .letterhead { left: 50px; top: 28px; width: 596px; height: 842px; }
  .letterhead .brand { left: 38px; top: 44px; }
  .letterhead .brand-name { font-size: 25px; }
  .letterhead .contact {
    position: absolute; right: 26px; top: 43px;
    text-align: right; font-size: 10.5px; line-height: 12.6px;
  }
  .letterhead .phone { font-size: 13px; margin-top: 11px; line-height: 14px; }
  .letterhead .web {
    position: absolute; left: 0; right: 0; top: 799px;
    text-align: center; font-size: 11.5px; letter-spacing: 0.4px; color: #555;
  }
  .letterhead .rule { left: 32px; right: 32px; top: 817px; }

  /* Business card front */
  .card-front { left: 557px; top: 291px; width: 256px; height: 147px; overflow: hidden; }
  .card-front .band {
    position: absolute; left: 0; top: 0; width: 100%; height: 50px;
    background: var(--card-dark);
  }
  .card-front .person { position: absolute; left: 17px; top: 18px; }
  .card-front .person-name { color: var(--green); font-size: 11px; line-height: 12px; }
  .card-front .person-role { color: var(--paper); font-size: 7.5px; line-height: 9px; }
  .card-front .brand { right: 14px; top: 13px; gap: 5px; }
  .card-front .brand-name { font-size: 13px; color: var(--paper); }
  .card-front .contact {
    position: absolute; left: 15px; top: 63px; font-size: 7.2px; line-height: 9.5px;
  }
  .card-front .phone { font-size: 10px; margin-top: 4px; line-height: 11px; }
  .card-front .web { position: absolute; right: 14px; top: 129px; font-size: 7.2px; }

  /* Business card back */
  .card-back {
    left: 835px; top: 295px; width: 252px; height: 143px;
    background: var(--card-dark);
  }
  .card-back .mark { position: absolute; left: 92px; top: 22px; }
  .card-back .tagline {
    position: absolute; left: 0; right: 0; top: 105px;
    text-align: center; color: var(--muted); font-size: 9px; line-height: 12.5px; font-weight: 300;
  }

  /* Compliment slip */
  .comp-slip { left: 516px; top: 482px; width: 596px; height: 280px; }
  .comp-slip .brand { left: 31px; top: 23px; }
  .comp-slip .brand-name { font-size: 25px; }
  .comp-slip .headline {
    position: absolute; right: 47px; top: 42px;
    color: var(--green); font-size: 20px; font-weight: 300; letter-spacing: 0.3px;
  }
  .comp-slip .contact {
    position: absolute; left: 30px; top: 146px; font-size: 10.5px; line-height: 12.5px;
  }
  .comp-slip .phone { font-size: 13px; margin-top: 7px; line-height: 14px; }
  .comp-slip .web {
    position: absolute; right: 47px; top: 231px; font-size: 11.5px; letter-spacing: 0.4px; color: #555;
  }
  .comp-slip .rule { left: 28px; right: 35px; top: 253px; }
</style>
</head>
<body>

<section class="sheet letterhead">
  <div class="brand">
    <svg width="40" height="40" viewBox="0 0 40 40" aria-hidden="true"><circle cx="20" cy="20" r="16" fill="none" stroke="var(--green)" stroke-width="5"/></svg>
    <span class="brand-name">brookfieldweb</span>
  </div>
  <address class="contact" style="font-style:normal">
    <div class="office">Ashford Head Office</div>
    <div class="address">Floor 2,<br>24 Abbey Lane,<br>Ashford,<br>AF2 3QB</div>
    <div class="phone">0854 311 5902</div>
    <div class="email">hello@brookfieldweb.co.uk</div>
  </address>
  <div class="web">www.<span class="web-accent">brookfieldweb</span>.co.uk</div>
  <div class="rule"></div>
</section>

<section class="sheet card-front">
  <div class="band"></div>
  <div class="person">
    <div class="person-name">Daniel Marsh</div>
    <div class="person-role">General manager</div>
  </div>
  <div class="brand">
    <svg width="20" height="20" viewBox="0 0 20 20" aria-hidden="true"><circle cx="10" cy="10" r="8" fill="none" stroke="var(--green)" stroke-width="2.5"/></svg>
    <span class="brand-name">brookfieldweb</span>
  </div>
  <address class="contact" style="font-style:normal">
    <div class="office">Ashford Head Office</div>
    <div class="address">Floor 2,<br>24 Abbey Lane,<br>Ashford,<br>AF2 3QB</div>
    <div class="phone">0854 311 5902</div>
    <div class="email">hello@brookfieldweb.co.uk</div>
  </address>
  <div class="web">www.<span class="web-accent">brookfieldweb</span>.co.uk</div>
</section>

<section class="sheet card-back">
  <svg class="mark" width="68" height="68" viewBox="0 0 68 68" aria-hidden="true"><circle cx="34" cy="34" r="28" fill="none" stroke="var(--green)" stroke-width="8"/></svg>
  <p class="tagline">We fuel search engine<br>marketing for higher <span class="web-accent">profits</span></p>
</section>

<section class="sheet comp-slip">
  <div class="brand">
    <svg width="40" height="40" viewBox="0 0 40 40" aria-hidden="true"><circle cx="20" cy="20" r="16" fill="none" stroke="var(--green)" stroke-width="5"/></svg>
    <span class="brand-name">brookfieldweb</span>
  </div>
  <h2 class="headline" style="font-weight:300">With Compliments</h2>
  <address class="contact" style="font-style:normal">
    <div class="office">Ashford Head Office</div>
    <div class="address">Floor 2,<br>24 Abbey Lane,<br>Ashford,<br>AF2 3QB</div>
    <div class="phone">0854 311 5902</div>
    <div class="email">hello@brookfieldweb.co.uk</div>
  </address>
  <div class="web">www.<span class="web-accent">brookfieldweb</span>.co.uk</div>
  <div class="rule"></div>
</section>

</body>
</html>
```